Town of Merrowfield Commercial Development

Create introduction point with 3 subheading categories. The bullets under the 3 categories should be where to use the infographics. Keep the Town of Merrowfield logo in the piece. The layout can be vertical or horizontal. Would like to stay on one page.

Target Market(s)

Commercial real estate developers and corporations

Industry/Entity Type

Real estate

Font styles to use
Serif

Requirements
Must have
• Business to business looking
Should not have
• Not comical

```html
<!DOCTYPE html>
<html lang="en">
<head>
<meta charset="utf-8">
<title>Town of Merrowfield – Commercial Development</title>
<link rel="stylesheet" href="https://fonts.googleapis.com/css2?family=Tinos:ital,wght@0,400;0,700;1,400&family=Arimo:wght@400&display=swap">
<style>
  :root {
    --red: #be1a24;
    --black: #050505;
    --white: #ffffff;
    --bg: #f4f4f4;
    --brown: #6b2a1a;
    --ink: #1a1a1a;
    --text-light: #ececec;
  }
  * { box-sizing: border-box; margin: 0; padding: 0; }
  html, body { width: 1000px; height: 1200px; overflow: hidden; background: var(--bg); }
  .canvas { position: relative; width: 1000px; height: 1200px; }
  .sheet {
    position: absolute; left: 204px; top: 180px; width: 594px; height: 842px;
    background: var(--white); border-bottom: 3px solid var(--red); overflow: hidden;
  }
  .brand { position: absolute; left: 62px; top: 78px; width: 170px; text-align: center; font-family: "Tinos", serif; color: var(--brown); }
  .brand-mark { display: block; margin: 0 auto 12px; width: 26px; height: 26px; border-radius: 50%; background: var(--brown); }
  .brand-name { font-size: 27px; line-height: 1.05; font-weight: 700; }
  .brand-tagline { margin-top: 10px; font-size: 9px; color: var(--ink); font-family: "Tinos", serif; }
  .intro {
    position: absolute; left: 282px; top: 58px; width: 262px;
    font-family: "Tinos", serif; font-style: italic; font-size: 13.6px; line-height: 22.3px; color: var(--ink);
  }
  .band { position: absolute; height: 169px; background: var(--black); }
  .band--left { left: 124px; width: 470px; border-radius: 30px 0 0 30px; }
  .band--right { left: 0; width: 469px; border-radius: 0 30px 30px 0; }
  .badge { position: absolute; width: 146px; height: 146px; border-radius: 50%; background: var(--white); }
  .badge-core { position: absolute; left: 9px; top: 9px; width: 128px; height: 128px; border-radius: 50%; background: var(--red); display: flex; align-items: center; justify-content: center; }
  .heading {
    position: absolute; font-family: "Tinos", serif; font-weight: 700; font-size: 11.5px; letter-spacing: 0.6px; color: var(--white);
    display: flex; align-items: center; gap: 8px;
  }
  .heading::after, .heading.rule-before::before { content: ""; display: block; height: 1px; background: var(--red); }
  .heading::after { width: 92px; }
  .heading.rule-before::after { display: none; }
  .heading.rule-before::before { width: 90px; }
  .points { position: absolute; list-style: none; font-family: "Arimo", sans-serif; font-size: 7.3px; line-height: 8.6px; color: var(--text-light); }
  .points li { position: relative; margin-bottom: 5px; }
  .points--left li { padding-left: 11px; }
  .points--right li { padding-right: 12px; text-align: right; }
  .points li::before {
    content: ""; position: absolute; top: 1.5px; width: 5px; height: 5px; border-radius: 50%;
    background: var(--red); box-shadow: 0 0 0 1px var(--black), 0 0 0 1.6px var(--red);
  }
  .points--left li::before { left: 0; }
  .points--right li::before { right: 0; }
</style>
</head>
<body>
<div class="canvas">
  <div class="sheet">
    <header>
      <div class="brand">
        <span class="brand-mark"></span>
        <div class="brand-name">Town of Merrowfield</div>
        <div class="brand-tagline">Room to Grow. Ready to Build.</div>
      </div>
      <p class="intro">Locating your business to Merrowfield could be the smartest move your company ever makes. Our location, employment base, smart growth and college town charm make it a stand-out from other communities.</p>
    </header>

    <section class="category" aria-label="Location">
      <div class="band band--left" style="top:223px"></div>
      <div class="badge" style="left:36px;top:235px"><div class="badge-core">
        <svg width="60" height="68" viewBox="0 0 60 68" fill="none" stroke="#fff" stroke-width="2.4"><path d="M30 64C30 64 6 38 6 24a24 24 0 0 1 48 0c0 14-24 40-24 40z"/><circle cx="30" cy="24" r="10"/></svg>
      </div></div>
      <h2 class="heading" style="left:214px;top:245px">LOCATION</h2>
      <ul class="points points--left" style="left:212px;top:269px;width:330px">
        <li>Merrowfield is just 20 miles north of Kingsbridge, NC in Alder County</li>
        <li>Conveniently located off I-41 and 58</li>
        <li>Within a day’s drive of 40% of the U.S. population, making business close to suppliers and customers alike</li>
        <li>30 minutes from Kingsbridge Regional Airport</li>
        <li>Located in the Kingsbridge MSA</li>
        <li>Home of Merrowfield College</li>
        <li>Three hours to beautiful beaches, two hours to scenic mountains</li>
      </ul>
    </section>

    <section class="category" aria-label="Community">
      <div class="band band--right" style="top:432px"></div>
      <div class="badge" style="left:409px;top:444px"><div class="badge-core">
        <svg width="64" height="64" viewBox="0 0 64 64" fill="none" stroke="#fff" stroke-width="1.8">
          <circle cx="32" cy="30" r="9"/><circle cx="32" cy="27" r="3"/><path d="M26 36c2-4 10-4 12 0"/>
          <circle cx="8" cy="8" r="6"/><circle cx="32" cy="6" r="4"/><circle cx="56" cy="8" r="6"/>
          <circle cx="8" cy="56" r="6"/><circle cx="32" cy="58" r="4"/><circle cx="56" cy="56" r="6"/>
          <circle cx="6" cy="32" r="3"/><circle cx="58" cy="32" r="3"/>
          <path d="M13 13l12 11M51 13L39 24M13 51l12-12M51 51L39 39M32 10v11M32 39v15M9 32h14M41 32h14"/>
        </svg>
      </div></div>
      <h2 class="heading rule-before" style="left:196px;top:456px">COMMUNITY</h2>
      <ul class="points points--right" style="left:103px;top:480px;width:280px">
        <li>Merrowfield is one of the fastest growing affluent populations in North Carolina with a median income of $131,144 and population of 15,132</li>
        <li>More than 74% of Merrowfield’s residents over the age of 25 hold a bachelor’s degree or higher</li>
        <li>In national citizen surveys, Merrowfield ranks #1 in “sense of community”</li>
        <li>Merrowfield’s lake amenities, parks, greenways, first-rate schools, low crime rate and proximity to Merrowfield College make it a great place to live and work.</li>
      </ul>
    </section>

    <section class="category" aria-label="Business">
      <div class="band band--left" style="top:642px"></div>
      <div class="badge" style="left:36px;top:654px"><div class="badge-core">
        <svg width="72" height="48" viewBox="0 0 72 48" fill="none" stroke="#fff" stroke-width="2.2" stroke-linejoin="round" stroke-linecap="round">
          <path d="M2 10l10-6 8 18-10 6z"/><path d="M70 10l-10-6-8 18 10 6z"/>
          <path d="M20 21l8-7c4-3 9-3 13-1l11 8"/>
          <path d="M12 27l14 14c2 2 5 2 7 0M19 32l10 10c2 2 5 2 7 0M26 29l12 12c2 2 5 2 6-1M32 26l12 12c2 2 5 0 4-3L36 22"/>
          <path d="M41 13l-9 7c-2 2 0 5 3 4l6-4"/>
        </svg>
      </div></div>
      <h2 class="heading" style="left:211px;top:669px">BUSINESS</h2>
      <ul class="points points--left" style="left:212px;top:693px;width:330px">
        <li>Merrowfield’s major employers include Corvane Systems, Halden Industrial Supply, Brightwell Tools, and Merrowfield College.</li>
        <li>Merrowfield has a thriving Farmer’s Market and is home to over 30 restaurants including Golden Ladle Award nominees.</li>
        <li>Merrowfield promotes a culture of supporting local independent businesses through our active business retention program, various funding programs, and small business networking opportunities.</li>
      </ul>
    </section>
  </div>
</div>
</body>
</html>
```